Flyer Design Project

Training and Consulting Flyer

I attached a document that contained the wording for the flyer as well as the logo.

Target Market(s)

Little Compass agencies and grantees

Industry/Entity Type

Training

Font styles to use
Sans Serif

Colors
e667a6
eda3c7
a54499
b768aa
f9d9e8

Requirements
Must have
• Words provided on attachment
Nice to have
• Graphics that are related to adult training/learning and consulting

```html
<!DOCTYPE html>
<html lang="en">
<head>
<meta charset="utf-8">
<title>Brightpath Health Consultants – Training &amp; Consulting Flyer</title>
<link rel="stylesheet" href="https://fonts.googleapis.com/css2?family=Open+Sans:wdth,wght@75..100,300..800&display=swap">
<style>
  :root {
    --pink: #e667a6;
    --pink-soft: #eda3c7;
    --purple: #a54499;
    --purple-light: #b768aa;
    --blush: #f9d9e8;
    --ink: #333333;
    --footer: #444444;
    --page: #e9e9ea;
    --white: #ffffff;
  }
  * { margin: 0; padding: 0; box-sizing: border-box; }
  html, body {
    width: 805px; height: 1200px; overflow: hidden;
    background: var(--page);
    font-family: "Open Sans", Arial, sans-serif;
    color: var(--ink);
  }
  .flyer {
    position: absolute;
    left: 32px; top: 121px;
    width: 435px; height: 563px;
    background: var(--white);
    transform: scale(1.7);
    transform-origin: top left;
    box-shadow: 0 2px 4px rgba(0,0,0,.15);
    overflow: hidden;
  }
  .hero { position: absolute; left: 0; top: 0; width: 435px; height: 195px; }
  .hero-photo {
    position: absolute; left: 140px; top: 0; width: 295px; height: 195px;
    background: linear-gradient(120deg, #dfe3e8 0%, #c9d0da 45%, #b7a89c 70%, #e7e9ec 100%);
  }
  .hero-panel { position: absolute; left: 0; top: 0; width: 200px; height: 195px; }
  .brand {
    position: absolute; left: 16px; top: 20px;
    display: flex; align-items: center; gap: 6px;
  }
  .brand-dot { width: 14px; height: 14px; border-radius: 50%; background: var(--blush); }
  .brand-name {
    font-weight: 600; font-stretch: 75%;
    font-size: 14px; line-height: 14px; color: var(--blush);
    text-transform: uppercase; letter-spacing: .3px;
  }
  .brand-tagline {
    position: absolute; left: 30px; top: 66px;
    font-size: 8.5px; color: var(--blush); letter-spacing: .3px;
  }
  .hero-title {
    position: absolute; left: 16px; top: 92px;
    font-weight: 700; font-stretch: 80%;
    font-size: 19px; line-height: 25px; color: var(--blush);
    text-transform: uppercase;
  }
  .band { position: absolute; left: 0; top: 195px; width: 435px; height: 55px; display: flex; }
  .band-quote {
    width: 200px; background: var(--purple-light); color: var(--white);
    font-weight: 700; font-stretch: 80%; font-size: 18px; line-height: 21px;
    padding: 6px 0 0 12px; text-transform: uppercase; position: relative;
  }
  .band-quote .mark { font-size: 24px; font-family: Georgia, serif; vertical-align: -4px; }
  .band-note {
    flex: 1; background: var(--purple); color: var(--blush);
    font-weight: 700; font-size: 8.2px; line-height: 12px;
    padding: 8px 8px 0 8px; text-transform: uppercase;
  }
  .strip { position: absolute; background: var(--purple); }
  .strip-left { left: 0; top: 276px; width: 20px; height: 247px; }
  .strip-right { right: 0; top: 276px; width: 15px; height: 247px; }
  .about { position: absolute; left: 32px; top: 256px; width: 380px; }
  .about-title {
    font-size: 15px; font-stretch: 85%; color: var(--purple);
    text-transform: uppercase; line-height: 18px;
    border-bottom: 1px solid #999; width: 100px; padding-bottom: 1px;
  }
  .about-title b { font-weight: 700; }
  .about-title span { font-weight: 400; }
  .about-copy { margin-top: 8px; }
  .about-copy p {
    font-size: 7.4px; line-height: 10px; text-align: justify; margin-bottom: 6px; color: #3a3a3a;
  }
  .family-photo {
    position: absolute; left: 26px; top: 441px; width: 175px; height: 82px;
    background: linear-gradient(100deg, #cdb7a6 0%, #e9d6c8 40%, #b59a86 70%, #efe6df 100%);
  }
  .consultant { position: absolute; left: 210px; top: 436px; width: 200px; }
  .consultant-title {
    font-weight: 700; font-stretch: 85%; font-size: 11px; color: #222;
    text-transform: uppercase; border-left: 1.5px solid #333; padding-left: 5px;
  }
  .consultant-body { display: flex; gap: 6px; margin-top: 5px; }
  .portrait {
    width: 66px; height: 64px;
    background: linear-gradient(160deg, #dcd7cf 0%, #8b6a55 55%, #c9d6a3 100%);
    border: 1px solid #ddd;
  }
  .consultant-name { font-weight: 600; font-stretch: 85%; font-size: 10px; color: #333; text-transform: uppercase; }
  .contact-line { display: flex; align-items: flex-start; gap: 4px; font-size: 8.2px; line-height: 11px; margin-top: 3px; color: #333; }
  .contact-line svg { flex: none; margin-top: 1px; }
  .footer {
    position: absolute; left: 0; top: 532px; width: 435px; height: 28px;
    background: var(--footer); color: var(--white);
    display: flex; align-items: center; padding-left: 22px;
    font-size: 10px;
  }
  .footer-item { display: flex; align-items: center; gap: 5px; }
  .footer-divider { width: 1px; height: 16px; background: #888; margin: 0 7px; }
</style>
</head>
<body>
  <main class="flyer">
    <section class="hero">
      <div class="hero-photo" role="img" aria-label="Photo of smiling colleagues joining hands in a high five"></div>
      <svg class="hero-panel" viewBox="0 0 200 195" aria-hidden="true">
        <polygon points="0,0 180,0 195,78 137,195 0,195" fill="var(--pink-soft)"/>
        <polygon points="0,0 170,0 185,78 127,195 0,195" fill="var(--purple)"/>
      </svg>
      <div class="brand">
        <span class="brand-dot"></span>
        <span class="brand-name">Brightpath<br>Health<br>Consultants</span>
      </div>
      <p class="brand-tagline">TOGETHER WE CAN</p>
      <h1 class="hero-title">Health<br>Consultants<br>&amp; Group</h1>
    </section>

    <section class="band">
      <h2 class="band-quote"><span class="mark">“</span>Together We<br>Reach the Goal<span class="mark">”</span></h2>
      <p class="band-note">Innovative approaches to the meeting the 5 year finding measures in the content area of health, nutrition, oral health &amp; safety</p>
    </section>

    <div class="strip strip-left"></div>
    <div class="strip strip-right"></div>

    <section class="about">
      <h3 class="about-title"><b>About</b> <span>Us</span></h3>
      <div class="about-copy">
        <p>BRIGHTPATH HEALTH CONSULTANTS has embarked on a new methodology ensure programmes meet total requirments as presentated under health service programmes.</p>
        <p>Let us manage your health programme though remote and offsite measures to ensure total compliance and strategic methodology toward quality servce approaches.</p>
        <p>Let us provide consultants to mentor your health manager nutrition content specialist facilities safety manager. These support consultants are advanced level academias in their specialised areas of focus.</p>
        <p>let us provide evidenced based mock reviews for your programe to assist management staff in focus 1,focus 12,review strategies for 2018.</p>
        <p>let us provide 12 ta for any new health nutrition,safety staff to ensure they are fully prepaired to perform their job duties at their higest level of management approaches.</p>
      </div>
    </section>

    <div class="family-photo" role="img" aria-label="Photo of smiling parents with a baby"></div>

    <section class="consultant">
      <h3 class="consultant-title">Meet the Consultant</h3>
      <div class="consultant-body">
        <div class="portrait" role="img" aria-label="Portrait photo of the consultant"></div>
        <div class="consultant-info">
          <p class="consultant-name">Dana Morrow, CEO</p>
          <p class="contact-line">
            <svg width="8" height="8" viewBox="0 0 24 24"><path d="M6.6 10.8a15 15 0 0 0 6.6 6.6l2.2-2.2a1 1 0 0 1 1-.25 11.4 11.4 0 0 0 3.6.57 1 1 0 0 1 1 1V20a1 1 0 0 1-1 1A17 17 0 0 1 3 4a1 1 0 0 1 1-1h3.5a1 1 0 0 1 1 1c0 1.25.2 2.45.57 3.57a1 1 0 0 1-.25 1z" fill="#333"/></svg>
            (555)-0142000</p>
          <p class="contact-line">
            <svg width="8" height="8" viewBox="0 0 24 24"><rect x="6" y="2" width="12" height="6" fill="none" stroke="#333" stroke-width="2"/><rect x="2" y="8" width="20" height="9" rx="2" fill="#333"/><rect x="6" y="14" width="12" height="8" fill="#fff" stroke="#333" stroke-width="2"/></svg>
            (555)-0187300</p>
          <p class="contact-line">
            <svg width="8" height="9" viewBox="0 0 24 26"><path d="M12 1a8 8 0 0 0-8 8c0 6 8 15 8 15s8-9 8-15a8 8 0 0 0-8-8z" fill="none" stroke="#333" stroke-width="2"/><circle cx="12" cy="9" r="3" fill="#333"/></svg>
            P. O. Box 2210, Fairview,<br>GA 30000</p>
        </div>
      </div>
    </section>

    <footer class="footer">
      <span class="footer-item">
        <svg width="9" height="7" viewBox="0 0 24 18"><rect width="24" height="18" rx="2" fill="var(--pink-soft)"/><path d="M1 2l11 8 11-8" fill="none" stroke="var(--footer)" stroke-width="2"/></svg>
        brightpathconsult@mail.com
      </span>
      <span class="footer-divider"></span>
      <span class="footer-item">
        <svg width="9" height="9" viewBox="0 0 24 24"><circle cx="12" cy="12" r="10" fill="none" stroke="#ccc" stroke-width="2"/><ellipse cx="12" cy="12" rx="4" ry="10" fill="none" stroke="#ccc" stroke-width="2"/><path d="M2 12h20" stroke="#ccc" stroke-width="2"/></svg>
        www.brightpathconsultants.com
      </span>
    </footer>
  </main>
</body>
</html>
```